Redesign Of Flower Delivery Subscription Service Website

I need a revamped website of www.petal-rush.com

Please revamp current design using same content....

Target Market(s)

people who buy flowers. Brides, wedding planners, wedding photographer, married man, boyfriend, etc.

Industry/Entity Type

Florist

Number of Pages Required

5+ page

Colors

Designer to choose colors to be used in the design.

Requirements
Must have
• I need a revamped website of www.petal-rush.com
• Please revamp current design using same content....
Nice to have
Should not have

```html
<!DOCTYPE html>
<html lang="en">
<head>
<meta charset="utf-8">
<title>Petal Rush – San Diego Flower Company</title>
<link href="https://fonts.googleapis.com/css2?family=Lobster&family=Jost:wght@300;400;500;600&display=swap" rel="stylesheet">
<style>
:root{
  --ink:#2b2b2b;
  --muted:#8a8a8a;
  --green:#8ccf4d;
  --red:#e9524f;
  --coral:#e9726c;
  --page:#f6f6f6;
  --line:#e2e4e8;
  --night:#0c111d;
  --white:#ffffff;
}
*{box-sizing:border-box;margin:0;padding:0}
html,body{width:1200px;height:2657px;overflow:hidden}
body{position:relative;background:var(--page);font-family:'Jost',sans-serif;color:var(--ink)}
.abs{position:absolute}
.script{font-family:'Lobster',cursive;font-weight:400}

/* header + hero */
.hero{left:0;top:0;width:1200px;height:593px;background:linear-gradient(90deg,#ebe6e6 0%,#f2eeee 50%,#e9e3e3 100%)}
.hero-photo{right:120px;top:80px;width:360px;height:500px;background:radial-gradient(ellipse at 60% 70%,#c7345f 0%,#d45a7e 25%,rgba(233,200,210,0) 65%)}
.hero-photo-floor{left:380px;top:440px;width:500px;height:110px;background:radial-gradient(ellipse at 50% 55%,rgba(214,74,112,.55) 0%,rgba(233,220,224,0) 70%)}
.brand{left:162px;top:30px;display:flex;align-items:center;gap:10px}
.brand-dot{width:14px;height:14px;border-radius:50%;background:var(--green)}
.brand-name{font-size:30px;font-weight:400;letter-spacing:2px;color:#4a4a4a;line-height:1}
.brand-tag{left:170px;top:63px;font-size:10px;color:#555}
.nav{left:397px;top:47px;display:flex;gap:32px;font-size:11px;font-weight:600;letter-spacing:.3px}
.nav a{color:var(--ink);text-decoration:none}
.nav a.active{color:var(--green)}
.hero-title{left:162px;top:206px;font-size:70px;color:#2e2e2e;letter-spacing:1px}
.hero-sub{left:162px;top:314px;font-size:13px;font-weight:500}
.hero-price{left:162px;top:345px;font-size:13px;font-weight:500}
.hero-price span{color:#e0263a}

/* feature grid */
.tile{overflow:hidden}
.set-it{left:161px;top:710px;width:331px;height:330px;background:var(--red);color:var(--white);padding:36px 40px 36px 22px}
.set-it h2{font-size:38px;margin-bottom:24px}
.set-it p{font-size:11px;line-height:18px;margin-bottom:18px}
.btn{display:inline-block;font-size:10px;font-weight:600;padding:9px 18px;border:2px solid currentColor;letter-spacing:.3px}
.photo-lisianthus{left:492px;top:710px;width:546px;height:330px;background:linear-gradient(110deg,#efeff1 0%,#f4c7b9 35%,#f7d6c8 55%,#f3f0dc 80%,#ecedef 100%)}
.photo-roses{left:161px;top:1040px;width:546px;height:662px;background:radial-gradient(ellipse at 50% 28%,#e6836e 0%,#e9a696 18%,#6f9a55 32%,#dfe3e7 55%,#e3e6ea 100%)}
.making{left:161px;top:1394px;width:331px;height:308px;background:rgba(236,238,241,.92);padding:34px 30px 34px 22px}
.making h2{font-size:38px;margin-bottom:20px;color:#222}
.making p{font-size:11px;line-height:18px;margin-bottom:18px}
.making .btn{color:var(--ink)}
.chevron{left:707px;top:1040px;width:331px;height:331px;background:var(--green)}
.never{left:745px;top:1092px;width:255px;height:227px;background:var(--white);text-align:center;padding:24px 16px}
.never h3{font-size:22px;margin-bottom:14px}
.never p{font-size:10.5px;line-height:18px;color:var(--muted)}
.dash{display:block;width:26px;height:2px;background:var(--red);margin:20px auto 0}
.photo-tulips{left:707px;top:1371px;width:331px;height:331px;background:radial-gradient(ellipse at 55% 55%,#f0867c 0%,#e9736c 45%,#e76f69 100%)}

/* signup */
.signup{left:161px;top:1757px;width:877px;height:137px;border-top:3px solid var(--line);border-bottom:3px solid var(--line)}
.signup-title{left:31px;top:30px;font-size:38px;line-height:1}
.signup-sub{left:31px;top:72px;font-size:24px;font-weight:600}
.signup-input{left:407px;top:48px;width:352px;height:34px;background:var(--white);border:1px solid #ececec;font-size:10px;color:#aaa;padding:10px 14px}
.signup-btn{left:766px;top:48px;width:82px;height:34px;border:2px solid var(--ink);font-size:10px;font-weight:600;text-align:center;line-height:30px}

/* intro */
.intro-title{left:161px;top:1938px;width:450px;font-size:30px;font-weight:600;line-height:39px}
.intro-copy{left:636px;top:1942px;width:404px;font-size:11px;line-height:18px;color:var(--muted)}

/* cards */
.card{top:2091px;width:430px;height:197px;background:var(--white);text-align:center;padding:30px 18px}
.card h3{font-size:21px;margin-bottom:12px}
.card p{font-size:11px;line-height:18px;color:var(--muted)}
.card-one{left:161px}
.card-two{left:608px}

/* footer */
.footer{left:0;top:2288px;width:1200px;height:369px;background:var(--night);color:#d9dce3}
.footer-map{left:220px;top:0;width:780px;height:369px;background:radial-gradient(ellipse at 50% 50%,#141b2b 0%,rgba(12,17,29,0) 70%)}
.footer h4{font-size:14px;font-weight:600;color:var(--white);margin-bottom:10px}
.footer ul{list-style:none}
.footer li,.footer p{font-size:10.5px;line-height:18px}
.col-services{left:161px;top:50px}
.col-contact{left:373px;top:50px}
.col-offer{left:603px;top:50px;width:437px}
.footer-brand{left:0;top:228px;width:1200px;display:flex;justify-content:center;align-items:center;gap:10px}
.footer-brand .brand-name{color:var(--white)}
.footer-tag{left:0;top:268px;width:1200px;text-align:center;font-size:10px;color:#cfd3da}
.copyright{left:0;top:333px;width:1200px;text-align:center;font-size:10.5px;color:#cfd3da}
</style>
</head>
<body>

<section class="abs hero">
  <div class="abs hero-photo" role="img" aria-label="Photo of pink chrysanthemums in a crimson vase"></div>
  <div class="abs hero-photo-floor" role="img" aria-label="Loose pink chrysanthemum stems lying on a white shelf"></div>
</section>

<header>
  <div class="abs brand"><span class="brand-name">PETAL RUSH</span><span class="brand-dot"></span></div>
  <div class="abs brand-tag">San Diego Flower Company</div>
  <nav class="abs nav">
    <a class="active" href="#">HOME</a>
    <a href="#">HOW IT WORK</a>
    <a href="#">DELIVERY AREA</a>
    <a href="#">FRANCHISE</a>
    <a href="#">MY ACCOUNT</a>
    <a href="#">BLOG</a>
    <a href="#">FREE FLOWER MON</a>
  </nav>
</header>

<h1 class="abs script hero-title">ALWAYS FRESH</h1>
<p class="abs hero-sub">Beautiful Flower Arrangements Delivered Monthly</p>
<p class="abs hero-price">Now only <span>$69.95/MTH ($100 value)</span></p>

<div class="abs tile set-it">
  <h2 class="script">Set it &amp; forget it</h2>
  <p>PetalRush is a “SET IT and FORGET IT” subscription based flower delivery service.</p>
  <p>For an Amazing price PetalRush will hand deliver a gorgeous arrangement directly to anyone you want every month without you having to worry about it.</p>
  <span class="btn">LEARN MORE</span>
</div>
<div class="abs tile photo-lisianthus" role="img" aria-label="Photo of pink and cream lisianthus flowers"></div>

<div class="abs tile photo-roses" role="img" aria-label="Photo of a bouquet of coral roses with greenery"></div>
<div class="abs tile making">
  <h2 class="script">Making Someone’s</h2>
  <p>day better Be the hero in that special someone’s life each and every month.</p>
  <p>It feels good to make a difference in your loved ones day.</p>
  <span class="btn">LEARN MORE</span>
</div>

<div class="abs tile chevron" role="img" aria-label="Green and white zigzag pattern frame"></div>
<div class="abs never">
  <h3 class="script">But never forget again</h3>
  <p>When setting up your account, you can choose exact delivery dates for the months that have special days such as your Anniversary, Birthday, Valentines Day and Mothers Day.</p>
  <span class="dash"></span>
</div>
<div class="abs tile photo-tulips" role="img" aria-label="Photo of coral tulips wrapped in paper"></div>

<section class="abs signup">
  <div class="abs script signup-title">Enter Your Email To</div>
  <div class="abs signup-sub">Receive A Free Upgrade</div>
  <div class="abs signup-input">Enter your email addess</div>
  <div class="abs signup-btn">SUBMIT</div>
</section>

<h2 class="abs intro-title">Monthly Subscription Based Flower Delivery Service in San Diego – CA by Our Florist Shop</h2>
<p class="abs intro-copy">Every moment of life could be cherished perfectly…….IF you choose wisely. To make your day more treasured, remember that flowers are the smartest choice when delivered through our monthly PetalRush subscription based delivery service. Our online subscription-based flower delivery service can help you pamper, cherish and make an everlasting impression on the minds of your loved ones with a doorstep delivery of exquisitely hand-designed floral arrangements.</p>

<article class="abs card card-one">
  <h3 class="script">Exotic Flowers Garnished With Special</h3>
  <p>Hues To Compliment Your Loved Ones<br>Let’s not forget a single day in which you can make your loved ones feel special. Whether it’s your anniversary or a birthday in your family, you must always go an extra mile to show “how much I care about you.”</p>
  <span class="dash"></span>
</article>
<article class="abs card card-two">
  <h3 class="script">Standard &amp; Personalized Flower Arrangement</h3>
  <p>For Special OccasionsPetalRush offers on time subscription based service that is risk free, trouble free and affordable at the same time. We offer the most trusted and delightful flower delivery service in San Diego, and are designed to deliver your…</p>
  <span class="dash"></span>
</article>

<footer class="abs footer">
  <div class="abs footer-map" role="img" aria-label="Faint dotted world map"></div>
  <div class="abs col-services">
    <h4>More Services</h4>
    <ul><li>Corporate Arrangements</li><li>Hotel Arrangements</li><li>Events</li><li>Weddings</li></ul>
  </div>
  <div class="abs col-contact">
    <h4>Contact Us</h4>
    <p>1480 Garden Row Way,<br>Fairhaven CA 90415<br>01234 000111<br>support@petalrushsd.com</p>
  </div>
  <div class="abs col-offer">
    <h4>Get Yourself Subscribed And Claim Discounts On Big Orders!</h4>
    <p>Get love and adulation by gifting flowers to your loved ones on those special occasions. Whether it’s formal, personal or your love for your family, just follow the subscription criteria and get your hands on the most valuable service for all kinds of events, occasions and parties. Set up your account and select the right delivery dates for the special months and leave the rest to us. We will deliver your flowers on the exact special dates to make your loved one’s day wonderful…</p>
  </div>
  <div class="abs footer-brand"><span class="brand-name">PETAL RUSH</span><span class="brand-dot"></span></div>
  <div class="abs footer-tag">San Diego Flower Company</div>
  <div class="abs copyright">Copyrights © 2018 Petal Rush, allrights are Reserved.</div>
</footer>

</body>
</html>
```